Cover for CD-single

TOVA is a young singer-songwriter and needs a CD cover design for her first single "Stars over harbour". Her song is about her best friend who recently moved from Europe to Australia with her family. But even though they now live on the other side of the world, they will always be there for each other.
You can use the picture attached or you can see it as an inspiration.
Please put the name of the artist: TOVA
and the name of the song on the cover: Stars over harbour

```html
<!DOCTYPE html>
<html lang="en">
<head>
<meta charset="utf-8">
<title>TOVA – Stars over harbour</title>
<link rel="stylesheet" href="https://fonts.googleapis.com/css2?family=Josefin+Sans:wght@400;600&display=swap">
<style>
  :root {
    --water-light: #756a3a;
    --water-mid: #5d522b;
    --water-deep: #3d2c15;
    --water-darkest: #2e2010;
    --photo-light: #d2c398;
    --photo-mid: #a8976c;
    --photo-dark: #6f6246;
    --frame-line: rgba(235, 225, 200, 0.55);
    --type-light: #faf6ec;
  }
  html, body {
    margin: 0;
    padding: 0;
    width: 1200px;
    height: 1200px;
    overflow: hidden;
    background: var(--water-deep);
  }
  .cover {
    position: relative;
    width: 1200px;
    height: 1200px;
    overflow: hidden;
  }
  .cover-water {
    position: absolute;
    inset: 0;
    background:
      linear-gradient(180deg,
        var(--water-light) 0%,
        var(--water-mid) 38%,
        #4e4122 52%,
        var(--water-deep) 62%,
        var(--water-darkest) 100%);
  }
  .cover-frame {
    position: absolute;
    left: 67px;
    top: 45px;
    width: 1066px;
    height: 1110px;
    border: 1.5px solid var(--frame-line);
    box-sizing: border-box;
  }
  .cover-art {
    position: absolute;
    inset: 0;
  }
  .song-title {
    font-family: "Josefin Sans", sans-serif;
    font-weight: 600;
    font-size: 31px;
    letter-spacing: 5px;
    fill: var(--type-light);
    text-transform: uppercase;
  }
  .artist-name {
    position: absolute;
    left: 0;
    right: 0;
    top: 1010px;
    margin: 0;
    text-align: center;
    font-family: "Josefin Sans", sans-serif;
    font-weight: 400;
    font-size: 54px;
    letter-spacing: 6px;
    color: var(--type-light);
  }
</style>
</head>
<body>
  <main class="cover">
    <div class="cover-water" role="img" aria-label="Blurred photograph of dark rippling harbour water in olive and brown tones"></div>
    <div class="cover-frame"></div>

    <svg class="cover-art" width="1200" height="1200" viewBox="0 0 1200 1200">
      <defs>
        <linearGradient id="photoTone" x1="0" y1="0" x2="0" y2="1">
          <stop offset="0" stop-color="var(--photo-light)"/>
          <stop offset="0.35" stop-color="var(--photo-mid)"/>
          <stop offset="0.6" stop-color="#bfb088"/>
          <stop offset="1" stop-color="var(--photo-dark)"/>
        </linearGradient>
        <radialGradient id="photoShadow" cx="0.5" cy="0.5" r="0.5">
          <stop offset="0.9" stop-color="#000" stop-opacity="0.35"/>
          <stop offset="1" stop-color="#000" stop-opacity="0"/>
        </radialGradient>
        <path id="titleArc" d="M 262,624 A 338 338 0 0 1 938,624"/>
      </defs>

      <circle class="photo-shadow" cx="600" cy="628" r="318" fill="url(#photoShadow)"/>
      <circle class="photo-circle" cx="600" cy="624" r="306" fill="url(#photoTone)"
              role="img" aria-label="Sepia photograph of two friends embracing, seen from behind, looking out over a harbour town and hills"/>

      <text class="song-title" text-anchor="middle">
        <textPath href="#titleArc" startOffset="50%">Stars over harbour</textPath>
      </text>
    </svg>

    <h1 class="artist-name">TOVA</h1>
  </main>
</body>
</html>
```